Business Card Design - Construction Company

Torvane Construction is in need of a sharp, modern business card design that has an architectural/high fashion feel.

We are looking for a two sided card.

One side simple dark grey/black with some texture in the background. e.g. (a mosaic of simple interconnecting shapes or a shadow of the logo.) Something to draw attention and create interest.It will need to feature a large Torvane construction logo (files attached) in metallic gradient or plain white.

The other side should contain all of our information:

(in largest text)
Name of person
Torvane Construction Pty. Ltd.

Licensed builders specialising in:
- Bathrooms
- Kitchens
- Commercial interiors

(mid sized text)
Phone number
Fax number
person@torvaneconstruction.example.au
www. torvaneconstruction.example.au

(smaller text)
ABN: 47209836512
BSA license: xxx-xxxx
PO Box 8640 Dunmore QLD 4170 (address)

Target Market(s)

professional home and business owners

Industry/Entity Type

Construction

Requirements
Must have
• Must be bold, professional looking and modern.
Nice to have
• We are undecided as to what kind of printing we will go with.
Definitely square edged.
Probably high quality satin card.
We are also interested in designs that would work well on transparent or translucent plastic.
Ideally we would print two versions.
Should not have
• Nothing with an antique feel.
No wild colours. Small amounts of colour can be good in the right place.

```html
<!DOCTYPE html>
<html lang="en">
<head>
<meta charset="utf-8">
<title>Torvane Construction – Business Card</title>
<link rel="stylesheet" href="https://fonts.googleapis.com/css2?family=Orbitron:wght@500;700&family=Arimo:wght@400&display=swap">
<style>
  :root {
    --page: #ffffff;
    --card: #000000;
    --ink: #ffffff;
    --shadow: rgba(0, 0, 0, 0.45);
  }
  * { margin: 0; padding: 0; box-sizing: border-box; }
  html, body {
    width: 1200px; height: 900px; overflow: hidden;
    background: var(--page);
  }
  .stage { position: relative; width: 1200px; height: 900px; }
  .card {
    position: absolute; width: 250px; height: 410px;
    background: var(--card); color: var(--ink);
    box-shadow: 3px 4px 5px var(--shadow);
    overflow: hidden;
  }
  .card--back { left: 247px; top: 353px; }
  .card--front { left: 703px; top: 136px; }

  .identity {
    position: absolute; left: 8px; top: 21px;
    font-family: "Orbitron", sans-serif; font-weight: 500;
    font-size: 11px; letter-spacing: 0.7px; line-height: 18px;
  }
  .identity .pty { font-size: 9px; line-height: 10px; display: block; }

  .services {
    position: absolute; right: 13px; top: 105px; text-align: right;
    font-family: "Arimo", sans-serif; font-size: 14px; line-height: 17.5px;
  }
  .contact {
    position: absolute; left: 6px; top: 221px;
    font-family: "Arimo", sans-serif; font-size: 12px; line-height: 14.5px;
    border-collapse: collapse;
  }
  .contact th {
    font-weight: 400; font-size: 10.5px; text-align: right;
    width: 31px; padding-right: 6px; vertical-align: baseline;
  }
  .contact td { vertical-align: baseline; white-space: nowrap; }
  .contact .long { font-size: 10.8px; letter-spacing: -0.1px; }
  .legal {
    position: absolute; right: 13px; top: 347px; text-align: right;
    font-family: "Arimo", sans-serif; font-size: 9px; line-height: 12px;
  }

  .wordmark {
    position: absolute; left: 0; right: 0; top: 152px;
    display: flex; flex-direction: column; align-items: center;
    font-family: "Orbitron", sans-serif; font-weight: 700;
  }
  .wordmark .dot {
    width: 62px; height: 62px; border-radius: 50%;
    border: 6px solid var(--ink); margin-bottom: 10px;
  }
  .wordmark .name { font-size: 26px; letter-spacing: 1.5px; line-height: 28px; }
  .wordmark .sub { font-size: 9px; letter-spacing: 2.5px; line-height: 12px; }
</style>
</head>
<body>
<main class="stage">
  <section class="card card--back" aria-label="Business card, information side">
    <p class="identity">NAME OF PERSON<br>TORVANE CONSTRUCTION<span class="pty">PTY. LTD.</span></p>
    <p class="services">Licensed builders<br>specialising in:<br>Bathrooms; Kitchens<br>&amp; Commercial interiors</p>
    <table class="contact">
      <tr><th>tel:</th><td>0123456789</td></tr>
      <tr><th>fax:</th><td>0123456789</td></tr>
      <tr><th>email:</th><td class="long">person@torvaneconstruction.example.au</td></tr>
      <tr><th>web:</th><td class="long">www.torvaneconstruction.example.au</td></tr>
    </table>
    <p class="legal">PO Box 8640<br>Dunmore QLD 4170<br>ABN: 47209836512<br>BSA license: xxx-xxxx</p>
  </section>

  <section class="card card--front" aria-label="Business card, brand side">
    <div class="wordmark">
      <span class="dot" aria-hidden="true"></span>
      <span class="name">TORVANE</span>
      <span class="sub">CONSTRUCTION</span>
    </div>
  </section>
</main>
</body>
</html>
```